Business Card

I need a business card that really pops for a potential customer or person who refers a personal injury lead. I want to highlight our office locations, but only address that needs to be on the card is my office's main address. I want a sleek, modern and minimalist design.

```html
<!DOCTYPE html>
<html lang="en">
<head>
<meta charset="utf-8">
<title>Prairie Injury Lawyers — Business Card</title>
<link href="https://fonts.googleapis.com/css2?family=Montserrat:wght@400;500;600&display=swap" rel="stylesheet">
<style>
  :root {
    --backdrop: #161616;
    --card: #333333;
    --card-back: #303030;
    --ink: #f4f4f4;
    --ink-soft: #e6e6e6;
    --muted: #595959;
  }
  html, body { margin: 0; padding: 0; }
  body {
    width: 1200px; height: 1059px; overflow: hidden;
    background: var(--backdrop);
    font-family: "Montserrat", sans-serif;
    position: relative;
  }
  .card {
    position: absolute;
    border-radius: 18px;
    background: var(--card);
  }
  .card--front { left: 257px; top: 89px; width: 687px; height: 390px; }
  .card--back { left: 254px; top: 547px; width: 693px; height: 394px; background: var(--card-back); }

  .firm-name {
    position: absolute; left: 0; right: 0;
    text-align: center; font-weight: 500; line-height: 1;
  }
  .card--front .firm-name { top: 100px; font-size: 32px; color: var(--ink); }
  .card--back .firm-name { top: 176px; font-size: 40px; color: var(--muted); }

  .person {
    position: absolute; right: 364px; top: 226px;
    text-align: right; color: var(--ink);
  }
  .person__name { font-size: 25px; font-weight: 600; letter-spacing: 1px; line-height: 1; }
  .person__role { font-size: 15.5px; font-weight: 400; margin-top: 9px; color: var(--ink-soft); }

  .divider {
    position: absolute; left: 343px; top: 223px;
    width: 1px; height: 57px; background: var(--ink-soft);
  }

  .contacts {
    position: absolute; left: 371px; top: 215px;
    list-style: none; margin: 0; padding: 0;
    color: var(--ink-soft); font-size: 16px;
  }
  .contacts li { display: flex; align-items: center; height: 23.5px; white-space: nowrap; }
  .contacts svg { width: 11px; height: 11px; margin-right: 8px; fill: var(--ink-soft); flex: none; }

  .address {
    position: absolute; left: 0; right: 0; top: 328px;
    text-align: center; color: var(--ink-soft); font-size: 15.5px;
  }
</style>
</head>
<body>
  <section class="card card--front">
    <div class="firm-name">Prairie Injury Lawyers</div>

    <div class="person">
      <div class="person__name">DANIEL HARLOW</div>
      <div class="person__role">CEO/Founder</div>
    </div>
    <div class="divider"></div>

    <ul class="contacts">
      <li>
        <svg viewBox="0 0 12 12" aria-hidden="true"><path d="M1 4.5C1 3 2.5 2 6 2s5 1 5 2.5V5H8.5V4H3.5v1H1z"/><rect x="2" y="6" width="8" height="4.5" rx="1"/></svg>
        (555) 382 4107
      </li>
      <li>
        <svg viewBox="0 0 12 12" aria-hidden="true"><path d="M1 4.5 6 1l5 3.5V11H1z M2 5l4 3 4-3" stroke="#333" stroke-width="0.8"/></svg>
        info@prairieinjury.com
      </li>
      <li>
        <svg viewBox="0 0 12 12" aria-hidden="true"><circle cx="6" cy="6" r="5"/><path d="M1 6h10M6 1c-2 2-2 8 0 10M6 1c2 2 2 8 0 10" stroke="#333" stroke-width="0.8" fill="none"/></svg>
        www.prairieinjury.com
      </li>
    </ul>

    <div class="address">2190 Linden Ave Oak Valley, 40218</div>
  </section>

  <section class="card card--back">
    <div class="firm-name">Prairie Injury Lawyers</div>
  </section>
</body>
</html>
```